Business Card and Simple Logo Desgin

New Zealand based start up company "Brava Advisory LTD" requires business cards and simple logo design.

Card Content.

Brava Advisory LTD

Rosalind Kettering
CA, BMS (Hons)

r.kettering@bravaadvisory.example.nz
PH +64 21 705 146

Target Market(s)

Corporate Business in IT, Finance and accounting.

Industry/Entity Type

Business

```html
<!DOCTYPE html>
<html lang="en">
<head>
<meta charset="utf-8">
<title>Brava Advisory LTD – Business Card</title>
<link rel="stylesheet" href="https://fonts.googleapis.com/css2?family=Marcellus&display=swap">
<style>
  :root {
    --card-bg: #000000;
    --gold-light: #f4dc9a;
    --gold: #d8b565;
    --gold-deep: #9a7430;
    --gold-text: #dcbd72;
  }
  html, body {
    margin: 0;
    padding: 0;
    width: 1200px;
    height: 777px;
    overflow: hidden;
    background: var(--card-bg);
  }
  .card {
    position: relative;
    width: 1200px;
    height: 777px;
    background: var(--card-bg);
    font-family: "Marcellus", "Times New Roman", serif;
    color: var(--gold-text);
  }
  .company-name {
    position: absolute;
    left: 33px;
    top: 118px;
    margin: 0;
    font-weight: 400;
    font-size: 100px;
    line-height: 137px;
    letter-spacing: 1px;
    color: var(--gold);
  }
  .company-name span {
    display: block;
  }
  .chain-band {
    position: absolute;
    left: 0;
    top: 410px;
    width: 1200px;
    height: 28px;
  }
  .contact {
    position: absolute;
    left: 31px;
    top: 474px;
    margin: 0;
    font-style: normal;
    font-size: 45px;
    line-height: 65px;
    color: var(--gold-text);
  }
  .contact p {
    margin: 0;
  }
</style>
</head>
<body>
  <main class="card">
    <h1 class="company-name">
      <span>Brava</span>
      <span>Advisory LTD</span>
    </h1>

    <svg class="chain-band" viewBox="0 0 1200 28" role="img" aria-label="Gold chain running across the card as a divider">
      <defs>
        <linearGradient id="chain-gold" x1="0" y1="0" x2="0" y2="1">
          <stop offset="0" stop-color="var(--gold-light)"/>
          <stop offset="0.5" stop-color="var(--gold)"/>
          <stop offset="1" stop-color="var(--gold-deep)"/>
        </linearGradient>
      </defs>
      <rect x="0" y="0" width="1200" height="28" fill="url(#chain-gold)"/>
    </svg>

    <address class="contact">
      <p class="contact-name">Rosalind Kettering</p>
      <p class="contact-credentials">CA, BMS (Hons)</p>
      <p class="contact-email">r.kettering@bravaadvisory.example.nz</p>
      <p class="contact-phone">PH +64 21 705 146</p>
    </address>
  </main>
</body>
</html>
```